Vital Spark Electrical in need of a business card design

We need a new business card designed for our electrical business. We have a logo already which I will attach below.
Would like the business card to be..
-BLACK background preferably, possibly white back ground behind logo if colours clash.
-White & Blue (logo blue) text
Something that makes the logo pop, & a modern look. Possibly minimal clean format.

REQUIRE:
-Logo on front & back

TEXT TO INCLUDE (ON ONE SIDE):

Tom Harlow
Director/Electrician
M: 0417 365 208
E:info@vitalsparkelectrical-example.com.au
W:www.vitalsparkelectrical-example.com.au
R.E.C 57318

Custom/New Homes
Renovations
Commercial Office/Shop Fit-outs
Communications & Security Cameras
Electric Vehicle Chargers
Airconditioning
Updates

Requirements
Nice to have
• Possibly even lighten the grey shades for the words 'Vital' & 'Spark' to be more easily read on a black background.

```html
<!DOCTYPE html>
<html lang="en">
<head>
<meta charset="UTF-8">
<title>Vital Spark Electrical – Business Card</title>
<link href="https://fonts.googleapis.com/css2?family=Montserrat:wght@400;500;700&display=swap" rel="stylesheet">
<style>
  :root {
    --backdrop: #141414;
    --card: #262627;
    --card-edge: #1a8fd6;
    --blue: #1ba3e3;
    --white: #f2f2f2;
    --grey-text: #d6d6d6;
    --rule: #6a6a6a;
    --logo-grey: #b9bec4;
  }
  * { box-sizing: border-box; margin: 0; padding: 0; }
  html, body {
    width: 1200px; height: 900px; overflow: hidden;
    background: var(--backdrop);
    font-family: "Montserrat", sans-serif;
  }
  .canvas {
    width: 1200px; height: 900px;
    display: flex; flex-direction: column;
    align-items: center; justify-content: center; gap: 44px;
  }
  .card {
    position: relative;
    width: 660px; height: 378px;
    background: var(--card);
    border-bottom: 4px solid var(--card-edge);
    border-left: 2px solid var(--card-edge);
    box-shadow: 0 18px 40px rgba(0,0,0,.6);
  }

  /* shared brand lockup */
  .brand { display: flex; align-items: center; gap: 12px; }
  .brand-mark { background: var(--blue); flex: none; }
  .brand-name { font-weight: 700; color: var(--logo-grey); letter-spacing: .01em; white-space: nowrap; }

  /* front */
  .card-front .brand { position: absolute; left: 62px; top: 56px; }
  .card-front .brand-mark { width: 22px; height: 22px; }
  .card-front .brand-name { font-size: 24px; }

  .person { position: absolute; left: 66px; top: 176px; }
  .person-name { font-size: 30px; font-weight: 700; color: var(--blue); line-height: 1.1; }
  .person-role { font-size: 17px; font-weight: 400; color: var(--grey-text); margin-top: 4px; }

  .divider { position: absolute; left: 66px; right: 70px; top: 250px; height: 1px; background: var(--rule); }

  .contact {
    position: absolute; right: 58px; top: 140px;
    list-style: none; text-align: right;
    font-size: 15px; font-weight: 400; color: var(--white);
  }
  .contact li { display: flex; align-items: center; justify-content: flex-end; gap: 10px; line-height: 28px; }
  .contact svg { width: 16px; height: 16px; stroke: var(--blue); fill: none; stroke-width: 1.6; flex: none; }
  .contact-wrap { position: absolute; right: 58px; top: 270px; }
  .contact-wrap .contact { position: static; }

  /* back */
  .card-back .brand { position: absolute; left: 0; right: 0; top: 110px; justify-content: center; gap: 18px; }
  .card-back .brand-mark { width: 40px; height: 40px; }
  .card-back .brand-name { font-size: 48px; }

  .services {
    position: absolute; right: 56px; top: 232px;
    list-style: none; text-align: right;
    font-size: 17px; font-weight: 400; color: var(--white); line-height: 30px;
  }
  .services .sep { color: var(--blue); padding: 0 8px; }
</style>
</head>
<body>
<main class="canvas">

  <section class="card card-front">
    <div class="brand">
      <span class="brand-mark"></span>
      <span class="brand-name">Vital Spark Electrical</span>
    </div>

    <div class="person">
      <p class="person-name">Tom Harlow</p>
      <p class="person-role">Director/Electrician</p>
    </div>

    <div class="divider"></div>

    <div class="contact-wrap">
      <ul class="contact">
        <li>0417 365 208
          <svg viewBox="0 0 16 16"><path d="M3 2h3l1.5 3.5-2 1.2a8 8 0 0 0 3.8 3.8l1.2-2L14 10v3a1 1 0 0 1-1 1A11 11 0 0 1 2 3a1 1 0 0 1 1-1z"/></svg>
        </li>
        <li>info@vitalsparkelectrical-example.com.au
          <svg viewBox="0 0 16 16"><rect x="1.5" y="3.5" width="13" height="9" rx="1"/><path d="M1.5 4l6.5 5 6.5-5"/></svg>
        </li>
        <li>www.vitalsparkelectrical-example.com.au
          <svg viewBox="0 0 16 16"><circle cx="8" cy="8" r="6.5"/><ellipse cx="8" cy="8" rx="3" ry="6.5"/><path d="M1.5 8h13"/></svg>
        </li>
      </ul>
    </div>
  </section>

  <section class="card card-back">
    <div class="brand">
      <span class="brand-mark"></span>
      <span class="brand-name">Vital Spark Electrical</span>
    </div>

    <ul class="services">
      <li>Commercial Office/Shop Fit-outs</li>
      <li>Custom/New Homes<span class="sep">|</span>Communications &amp; Security Cameras</li>
      <li>Renovations<span class="sep">|</span>Electric Vehicle Chargers<span class="sep">|</span>Airconditioning</li>
    </ul>
  </section>

</main>
</body>
</html>
```